Brevanta Interiors
Business Card, Stationery Package, Email Signature
Project: Brevanta Interiors
Brevanta Interiors -
Creative Brief
Professional
Marisol Pryde
Managing Director
P.O.Box 4372 Converse, TX 78109 - 4372
mpryde@brevantainteriors.example
www.brevantainteriors.example
Brevanta Interiors is a retail store offering Flooring products and Installation services. We would like to have the following items made: Business Card, Stationery Package (Fax, Letterhead, Envelopes, etc.), and Email Signature. We would like to see two types of fonts created for comparison, the original font and one of your own professional choices. Winner, please provide all design templates for future modification upon completion of the contest. Thank you!
logo, text, slogan, and web address.

```html
<!DOCTYPE html>
<html lang="en">
<head>
<meta charset="utf-8">
<title>Brevanta Interiors – Business Card</title>
<link href="https://fonts.googleapis.com/css2?family=Arimo:ital,wght@0,400;0,700;1,400;1,700&display=swap" rel="stylesheet">
<style>
  :root {
    --bg: #ece7e1;
    --card: #ffffff;
    --green: #3a9a3f;
    --blue: #1f4fa0;
    --ink: #444a52;
  }
  * { margin: 0; padding: 0; box-sizing: border-box; }
  html, body { width: 1200px; height: 463px; overflow: hidden; background: var(--bg); }
  body { position: relative; font-family: "Arimo", Arial, sans-serif; color: var(--ink); }

  .card {
    position: absolute; top: 40px; width: 470px; height: 390px;
    background: var(--card); border-radius: 26px; overflow: hidden;
    box-shadow: 0 4px 12px rgba(0,0,0,.18);
  }
  .card--front { left: 128px; }
  .card--back { left: 636px; }
  .card .swoosh { position: absolute; inset: 0; width: 100%; height: 100%; }

  .brand { position: absolute; display: flex; align-items: center; gap: 10px; }
  .brand__dot { width: 22px; height: 22px; border-radius: 50%; background: var(--blue); flex: none; }
  .brand__name { font-weight: 700; color: var(--green); letter-spacing: -0.5px; white-space: nowrap; }

  .card--front .brand { left: 30px; top: 112px; }
  .card--front .brand__name { font-size: 36px; }

  .tagline {
    position: absolute; left: 64px; top: 162px;
    font-size: 15px; font-weight: 700; letter-spacing: 5px; color: var(--blue);
  }
  .slogan {
    position: absolute; left: 200px; top: 188px;
    font-size: 15px; font-style: italic; font-weight: 700; color: var(--blue);
  }
  .person { position: absolute; left: 30px; top: 236px; font-size: 15px; }
  .person__name { color: var(--blue); font-weight: 700; }
  .address { position: absolute; left: 30px; top: 262px; font-size: 14px; }

  .contacts {
    position: absolute; left: 30px; top: 292px;
    display: grid; grid-template-columns: 130px auto; row-gap: 10px; column-gap: 8px;
    font-size: 13px;
  }
  .contact { display: flex; align-items: center; gap: 6px; white-space: nowrap; }
  .contact svg { width: 14px; height: 14px; flex: none; }

  .card--back .brand { left: 0; right: 0; top: 160px; justify-content: center; }
  .card--back .brand__name { font-size: 34px; }
  .card--back .web {
    position: absolute; left: 40px; width: 300px; top: 322px; text-align: center;
    font-size: 15px; color: var(--ink); white-space: nowrap;
  }
</style>
</head>
<body>

<section class="card card--front" aria-label="Business card front">
  <svg class="swoosh" viewBox="0 0 470 390" aria-hidden="true">
    <defs>
      <linearGradient id="greenFade" x1="0" y1="0" x2="1" y2="1">
        <stop offset="0" stop-color="#2f8a37"/><stop offset="1" stop-color="#8ccc60"/>
      </linearGradient>
      <linearGradient id="blueFade" x1="0" y1="0" x2="1" y2="1">
        <stop offset="0" stop-color="#4a9be0"/><stop offset="1" stop-color="#173f8c"/>
      </linearGradient>
    </defs>
    <path d="M0 0 H230 C150 10 60 40 0 110 Z" fill="url(#greenFade)"/>
    <path d="M470 250 C420 320 330 370 210 390 H470 Z" fill="url(#blueFade)"/>
  </svg>

  <div class="brand">
    <span class="brand__dot"></span>
    <span class="brand__name">Brevanta Interiors</span>
  </div>
  <p class="tagline">WOOD . TILE . CARPET</p>
  <p class="slogan">Floors Built Around You</p>

  <p class="person"><span class="person__name">Marisol Pryde</span> <span class="person__role">| Managing Director</span></p>
  <p class="address">P.O.Box 4372, Ridgehollow, TX 76514 - 4372</p>

  <div class="contacts">
    <span class="contact">
      <svg viewBox="0 0 16 16"><path fill="#3a9a3f" d="M3 1h3l1.5 4-2 1.3a9 9 0 0 0 4.2 4.2L11 8.5l4 1.5v3a2 2 0 0 1-2 2A12 12 0 0 1 1 3a2 2 0 0 1 2-2z"/></svg>
      210.555.0147
    </span>
    <span class="contact">
      <svg viewBox="0 0 16 16"><circle cx="8" cy="8" r="7" fill="#3a9a3f"/><path d="M4 6l4 3 4-3" stroke="#fff" stroke-width="1.4" fill="none"/></svg>
      mpryde@brevantainteriors.example
    </span>
    <span class="contact">
      <svg viewBox="0 0 16 16"><rect x="2" y="5" width="12" height="8" rx="1.5" fill="#3a9a3f"/><rect x="4" y="2" width="8" height="4" fill="#3a9a3f"/></svg>
      210.555.0193
    </span>
    <span class="contact">
      <svg viewBox="0 0 16 16"><circle cx="8" cy="8" r="7" fill="#3a9a3f"/><path d="M1 8h14M8 1c3 3 3 11 0 14M8 1c-3 3-3 11 0 14" stroke="#fff" stroke-width="1" fill="none"/></svg>
      www.brevantainteriors.example
    </span>
  </div>
</section>

<section class="card card--back" aria-label="Business card back">
  <svg class="swoosh" viewBox="0 0 470 390" aria-hidden="true">
    <path d="M0 0 H300 C190 20 70 80 0 180 Z" fill="url(#greenFade)"/>
    <path d="M470 200 C440 300 360 365 260 390 H470 Z" fill="url(#blueFade)"/>
  </svg>
  <div class="brand">
    <span class="brand__dot"></span>
    <span class="brand__name">Brevanta Interiors</span>
  </div>
  <p class="web">www.brevantainteriors.example</p>
</section>

</body>
</html>
```